Brisk Lending - Morgage Broker Website

Hi. I want someone to redesign my website for Brisk Lending, We are a mortgage brokering company in Australia.

I currently have a website www.brisklending.com.au but i do not like the design, I want clean but looking like a nice techie site but with that personal touch still.

I use wordpress and have Elementor Pro installed

Pages like on current site

Target Market(s)

Age Group 30-50, either home owners or looking to buy.

Coding

Coded - Design and coding required

Number of Pages Required

5+ page

Font styles to use
Other font styles liked:
• Ubuntu

Colors
e34298
a54499
e667a6
d3a5cc
b868aa
eea4c8

Requirements
Must have
• My Logo, and branding.. logo attached..
I want something clean and nice and vibrant!
Wordpress!
Mobile Friendly
Contact Forms
Appointment booking button
Call now button
Nice to have
• Mortgage Calculator section, and plenty of CTA's!.

Please do you research on other mortgage broker sites like varopa.com.au

```html
<!DOCTYPE html>
<html lang="en">
<head>
<meta charset="utf-8">
<title>Brisk Lending – Give us a chance</title>
<link rel="stylesheet" href="https://fonts.googleapis.com/css2?family=Ubuntu:wght@400;500;700&display=swap">
<style>
  :root {
    --ink-heading: #474c52;
    --ink-body: #2f3337;
    --white: #ffffff;
    --cta-orange: #ff7300;
    --icon-pink: #ff3d9a;
    --band-deep: #2a1418;
    --band-mid: #4a2124;
    --band-warm: #6b2a2a;
    --band-glow: #8a5a3a;
  }
  * { box-sizing: border-box; margin: 0; padding: 0; }
  html, body {
    width: 1200px;
    height: 675px;
    overflow: hidden;
    background: var(--white);
    font-family: "Ubuntu", sans-serif;
  }
  .page {
    position: relative;
    width: 1200px;
    height: 675px;
  }
  .intro {
    height: 300px;
    background: var(--white);
    text-align: center;
    padding-top: 96px;
  }
  .intro-title {
    font-size: 34px;
    font-weight: 700;
    color: var(--ink-heading);
    letter-spacing: 0.2px;
  }
  .intro-lede {
    margin-top: 22px;
    font-size: 15px;
    font-weight: 400;
    color: var(--ink-body);
  }
  .cta-book {
    display: inline-block;
    margin-top: 18px;
    width: 176px;
    height: 53px;
    line-height: 53px;
    background: var(--cta-orange);
    color: var(--white);
    font-size: 15px;
    font-weight: 500;
    text-transform: uppercase;
    text-decoration: none;
    border-radius: 3px;
  }
  .process {
    position: relative;
    height: 375px;
  }
  .process-photo {
    position: absolute;
    inset: 0;
    background:
      radial-gradient(ellipse 320px 260px at 900px 260px, var(--band-glow) 0%, transparent 70%),
      radial-gradient(ellipse 400px 300px at 250px 180px, #3b3032 0%, transparent 75%),
      linear-gradient(100deg, var(--band-deep) 0%, var(--band-mid) 45%, var(--band-warm) 75%, var(--band-mid) 100%);
  }
  .process-steps {
    position: absolute;
    left: 0;
    top: 120px;
    width: 1200px;
    height: 140px;
  }
  .step {
    position: absolute;
    top: 0;
    width: 180px;
    margin-left: -90px;
    text-align: center;
    color: var(--white);
  }
  .step svg {
    display: block;
    margin: 0 auto;
    width: 56px;
    height: 52px;
  }
  .step-label {
    margin-top: 24px;
    font-size: 15px;
    font-weight: 700;
    line-height: 21px;
  }
  .icon-line { fill: none; stroke: var(--icon-pink); stroke-width: 3; stroke-linecap: round; stroke-linejoin: round; }
  .icon-fill { fill: var(--icon-pink); }
</style>
</head>
<body>
<main class="page">
  <section class="intro">
    <h1 class="intro-title">Give us a chance to make a difference</h1>
    <p class="intro-lede">We’re all about helping you reach your next financial goal—great rates, less fees, unprecedented service, and awesome loan help.</p>
    <a class="cta-book" href="#book">Book in now</a>
  </section>

  <section class="process">
    <div class="process-photo" role="img" aria-label="Photo of a smiling couple looking at a screen together, with warm blurred city lights behind them"></div>
    <div class="process-steps">
      <div class="step" style="left:245px">
        <svg viewBox="0 0 56 52" aria-hidden="true">
          <circle class="icon-fill" cx="10" cy="7" r="5"/>
          <path class="icon-fill" d="M5 15h10v16h-2v19h-3V33H9v17H6V31H5z"/>
          <path class="icon-line" d="M14 20l14-6"/>
          <rect class="icon-line" x="26" y="4" width="27" height="22" rx="3"/>
        </svg>
        <p class="step-label">We listen to you and learn</p>
      </div>
      <div class="step" style="left:440px">
        <svg viewBox="0 0 56 52" aria-hidden="true">
          <circle class="icon-fill" cx="28" cy="7" r="6"/>
          <path class="icon-fill" d="M20 16h16l3 14 10 8-2 3-12-8-1-8v12h-12V29l-1 4-12 8-2-3 10-8z"/>
          <path class="icon-fill" d="M6 46c6-5 16-7 22-7s16 2 22 7l-2 3c-6-3-14-5-20-5s-14 2-20 5z"/>
        </svg>
        <p class="step-label">We create breathing space for you</p>
      </div>
      <div class="step" style="left:634px">
        <svg viewBox="0 0 56 52" aria-hidden="true">
          <rect class="icon-fill" x="6" y="34" width="6" height="12"/>
          <rect class="icon-fill" x="16" y="26" width="6" height="20"/>
          <rect class="icon-fill" x="26" y="30" width="6" height="16"/>
          <rect class="icon-fill" x="36" y="18" width="6" height="28"/>
          <rect class="icon-fill" x="46" y="12" width="6" height="34"/>
          <path class="icon-line" d="M3 49h51"/>
          <path class="icon-line" d="M6 26l12-10 10 6 18-16"/>
          <path class="icon-fill" d="M40 2h12v12z"/>
        </svg>
        <p class="step-label">We develop your Mortgage plan</p>
      </div>
      <div class="step" style="left:829px">
        <svg viewBox="0 0 56 52" aria-hidden="true">
          <rect class="icon-line" x="14" y="2" width="28" height="48" rx="3"/>
          <rect class="icon-line" x="19" y="7" width="18" height="9"/>
          <g class="icon-fill">
            <rect x="19" y="21" width="4" height="4"/><rect x="26" y="21" width="4" height="4"/><rect x="33" y="21" width="4" height="4"/>
            <rect x="19" y="29" width="4" height="4"/><rect x="26" y="29" width="4" height="4"/><rect x="33" y="29" width="4" height="4"/>
            <rect x="19" y="37" width="4" height="4"/><rect x="26" y="37" width="4" height="4"/><rect x="33" y="37" width="4" height="4"/>
          </g>
        </svg>
        <p class="step-label">We select the right financial institution</p>
      </div>
      <div class="step" style="left:1023px">
        <svg viewBox="0 0 56 52" aria-hidden="true">
          <path class="icon-line" d="M19 22V14a9 9 0 0 1 18 0v8" style="stroke-width:5"/>
          <rect class="icon-fill" x="12" y="22" width="32" height="28" rx="3"/>
          <circle cx="28" cy="33" r="3.5" fill="var(--white)"/>
          <rect x="26.5" y="34" width="3" height="8" fill="var(--white)"/>
        </svg>
        <p class="step-label">We help build your secure future</p>
      </div>
    </div>
  </section>
</main>
</body>
</html>
```